Marrowfield Contracting Business Cards

Front of card:

Full Logo
Name
Address
Office Phone
Cell Phone
Email
Website

Back:
Logo Mark in background
List and markets and services performed

```html
<!DOCTYPE html>
<html lang="en">
<head>
<meta charset="utf-8">
<title>Marrowfield Contracting Business Cards</title>
<link rel="stylesheet" href="https://fonts.googleapis.com/css2?family=Arimo:wght@400;700&display=swap">
<style>
  :root {
    --stage: #2b2b2b;
    --red: #c0181b;
    --red-deep: #a51215;
    --white: #ffffff;
    --paper: #f7f7f7;
    --grey: #6d6e70;
  }
  * { margin: 0; padding: 0; box-sizing: border-box; }
  html, body {
    width: 1200px; height: 768px; overflow: hidden;
    background: var(--stage);
    font-family: "Arimo", Arial, sans-serif;
  }
  .sheet {
    position: relative; width: 1200px; height: 768px;
    display: flex; align-items: center; justify-content: center; gap: 40px;
  }
  .card {
    position: relative; width: 540px; height: 309px;
    border-radius: 20px; overflow: hidden;
  }

  /* Back */
  .card-back {
    background: linear-gradient(160deg, #cf1e21 0%, var(--red) 50%, var(--red-deep) 100%);
  }
  .back-mark {
    position: absolute; left: 50%; top: 44%;
    width: 150px; height: 150px; margin: -75px 0 0 -75px;
    border-radius: 50%;
    border: 14px solid rgba(0,0,0,0.08);
    box-shadow: inset 0 1px 2px rgba(255,255,255,0.12);
  }
  .back-services {
    position: absolute; left: 0; right: 0; bottom: 40px;
    text-align: center; color: var(--white);
    font-size: 15px; letter-spacing: 0.3px;
  }

  /* Front */
  .card-front { background: var(--paper); }
  .front-band { position: absolute; inset: 0; width: 540px; height: 309px; }
  .holder { position: absolute; left: 28px; top: 22px; }
  .holder-name { color: var(--red); font-weight: 700; font-size: 20px; }
  .holder-title { color: var(--grey); font-size: 13px; margin-top: 1px; }
  .brand {
    position: absolute; left: 28px; top: 88px;
    display: flex; align-items: center; gap: 12px;
  }
  .brand-dot {
    width: 42px; height: 42px; border-radius: 50%; background: var(--red); flex: none;
  }
  .brand-name {
    color: var(--red); font-weight: 700; font-size: 20px;
    letter-spacing: 1.5px; text-transform: uppercase; line-height: 1.15;
  }
  .contacts {
    position: absolute; right: 26px; top: 186px;
    color: var(--white); font-size: 15px; line-height: 19px;
    text-align: right;
  }
  .contacts li { list-style: none; display: flex; align-items: center; justify-content: flex-end; gap: 8px; }
  .contacts svg { width: 12px; height: 12px; fill: var(--white); flex: none; }
  .address {
    position: absolute; right: 26px; bottom: 14px;
    color: var(--white); font-size: 15px;
  }
</style>
</head>
<body>
<main class="sheet">
  <section class="card card-back" aria-label="Card back">
    <div class="back-mark" aria-hidden="true"></div>
    <p class="back-services">List and markets and services performed</p>
  </section>

  <section class="card card-front" aria-label="Card front">
    <svg class="front-band" viewBox="0 0 540 309" aria-hidden="true">
      <defs>
        <linearGradient id="bandFill" x1="0" y1="0" x2="1" y2="1">
          <stop offset="0" stop-color="#c81c1f"/>
          <stop offset="1" stop-color="#a81215"/>
        </linearGradient>
      </defs>
      <path d="M0,171 C180,231 380,221 540,46 L540,309 L0,309 Z" fill="url(#bandFill)"/>
      <path d="M0,165 C180,225 380,215 540,40" fill="none" stroke="#c9c9c9" stroke-width="5"/>
      <path d="M0,168 C180,228 380,218 540,43" fill="none" stroke="#8f8f8f" stroke-width="1.5"/>
    </svg>

    <div class="holder">
      <p class="holder-name">Owen Hartley</p>
      <p class="holder-title">President</p>
    </div>

    <div class="brand">
      <span class="brand-dot" aria-hidden="true"></span>
      <span class="brand-name">Marrowfield<br>Contracting LLC</span>
    </div>

    <ul class="contacts">
      <li>(555) 0142-7731
        <svg viewBox="0 0 12 12"><path d="M2.5 1l2 2-1 1.5c.6 1.4 1.6 2.4 3 3l1.5-1 2 2-1.5 2C5 10.5 1.5 7 .5 2.5z"/></svg></li>
      <li>(555) 0142-7732
        <svg viewBox="0 0 12 12"><path d="M3 0h6a1 1 0 0 1 1 1v10a1 1 0 0 1-1 1H3a1 1 0 0 1-1-1V1a1 1 0 0 1 1-1zm.5 1.5v8h5v-8z"/></svg></li>
      <li>name@MARROWFIELD.com
        <svg viewBox="0 0 12 12"><path d="M0 2h12v8H0zm1 1v.4l5 3 5-3V3z"/></svg></li>
      <li>www.MARROWFIELD.com
        <svg viewBox="0 0 12 12"><circle cx="6" cy="6" r="5.5"/></svg></li>
    </ul>
    <p class="address">2710 Larchmont Drive, Elm Vale, NY 10987</p>
  </section>
</main>
</body>
</html>
```